Information Technology Company needs a Website...

We need a single page website for new technology company called:

MERIVALE CREST TECHNOLOGY GROUP
Based in Ojai CA.

We are offering three primary services:

- Business Solutions

- IT Services

- Software Implementation and Consulting

We want a single page design where all content scrolls down/up on one page. We're looking for the following characteristics:

- Home/Landing
- Active background with panoramic view (Will provide content)

- Business Solutions, IT Services, Software Implementation and Consulting

List of software vendors we recommend (Company logos)

- About
- History
- Our Team
- Partners

I'll upload our new logo as soon as we get the design files. I'll also send over some example website layout's that we like shortly.

Target Market(s)

Small/Medium Businesses

Industry/Entity Type

Information Technology

Number of Pages Required

1 page

Font styles to use
Other font styles liked:
• Sansation

Requirements
Must have
• Full page browser width, easy navigation and visibility. Creative design, not like every other "Technology" website template. Should be the "One Page" design where each section is below the next and the user scrolls down the page through the whole site. I like the concept of the following website in the main "Whiteboard" image:
• http://www.plinkoria-sample.com/design/4082913
• And the way this site does the active panoramic background:
• http://www.vantrelwork-sample.com/
• Something interesting and appealing to potential clients looking for Small/Medium business solutions and IT Services.
• Use uploaded Logo to establish color and theme for website.
Should not have
• Look the same as every other information technology website template.

```html
<!DOCTYPE html>
<html lang="en">
<head>
<meta charset="utf-8">
<title>Merivale Crest Technology Group</title>
<link href="https://fonts.googleapis.com/css2?family=Open+Sans:wght@400;600;700&family=Arimo:wght@400;700&display=swap" rel="stylesheet">
<style>
:root{
  --orange:#f4511e;
  --orange-light:#ff7a4f;
  --orange-text:#e8501f;
  --grey-text:#9a9a9a;
  --dark:#141414;
  --teal:#3bb39a;
  --page:#f3f3f3;
  --team-bg:#e4e4e4;
  --card:#c8c8c8;
  --lime:#8dc63f;
}
*{box-sizing:border-box;margin:0;padding:0}
html,body{width:1200px;height:2695px;overflow:hidden}
body{position:relative;background:var(--page);font-family:"Open Sans",sans-serif;color:#222}
.abs{position:absolute}

/* header */
.site-header{left:0;top:0;width:1200px;height:135px;background:linear-gradient(#ffffff,#f1f1f1)}
.brand{left:162px;top:30px;display:flex;align-items:center;gap:12px}
.brand-mark{width:22px;height:22px;background:var(--orange);border-radius:50%}
.brand-name{font-size:20px;font-weight:700;color:#4a4a4a;line-height:1.15;letter-spacing:.5px}
.enquiry{right:122px;top:34px;font-size:16px;color:#555}
.enquiry span{color:var(--orange);margin-left:14px}
.main-nav{right:122px;top:76px;display:flex;gap:30px;font-size:16px;color:var(--grey-text)}
.main-nav .active{color:var(--orange);position:relative}
.main-nav .active::after{content:"";position:absolute;left:-2px;right:-2px;top:41px;height:6px;background:var(--orange)}

/* hero */
.hero{left:0;top:135px;width:1200px;height:605px;background:linear-gradient(160deg,#d9c58a 0%,#c9b27a 25%,#a89c7c 55%,#8c8c80 80%,#6f7470 100%)}
.hero-panel{left:275px;top:314px;width:628px;height:271px;background:rgba(90,85,70,.55);display:flex;align-items:center;justify-content:center;text-align:center;color:#fff;font-size:60px;line-height:1.05}
.hero-caption{left:871px;top:648px;font-size:21px;color:#fff}
.hero-rule{left:0;top:738px;width:1200px;height:3px;background:var(--orange)}

/* who */
.pill{left:485px;top:713px;width:248px;height:45px;border-radius:14px;background:var(--orange);border:3px solid #fff;color:#fff;font-weight:700;font-size:22px;display:flex;align-items:center;justify-content:center}
.who-text{left:140px;top:793px;width:930px;text-align:center;font-size:19.5px;line-height:1.4;color:#222}

/* services */
.services{left:0;top:961px;width:1200px;height:535px;background:linear-gradient(#ff7b50,#f55a28 55%,#f4511e)}
.section-title{width:1200px;left:0;text-align:center;font-weight:700;font-size:25px}
.services .section-title{top:24px;color:#fff}
.service{width:280px;height:280px;border:3px solid #fff;border-radius:50%;color:#fff;text-align:center;top:113px}
.service svg{position:absolute;left:50%;top:42px;transform:translateX(-50%)}
.service h3{position:absolute;left:0;right:0;top:135px;font-size:15px;font-weight:700;line-height:1.05}
.service p{position:absolute;left:60px;right:60px;top:170px;font-size:10.5px;line-height:1.5}
.service.two h3{top:130px}
.service.two p{top:170px}
.more{width:80px;height:80px;border:2px solid #fff;border-radius:50%;color:#fff;font-size:11px;font-weight:700;display:flex;align-items:center;justify-content:center;top:355px}

/* team */
.team{left:0;top:1496px;width:1200px;height:507px;background:var(--team-bg)}
.team .section-title{top:20px;color:var(--orange-text)}
.member{top:88px;width:208px;height:320px;background:var(--card);border-radius:10px;overflow:hidden;text-align:center}
.member.current{background:#e9e9e9;border:3px solid #c9c9c9}
.avatar{position:absolute;left:36px;top:15px;width:136px;height:136px;border-radius:50%;border:4px solid #fff;background:radial-gradient(circle at 50% 40%,#c98f75,#8a4e3a)}
.member h4{position:absolute;left:0;right:0;top:145px;color:var(--orange-text);font-size:19px;font-weight:700}
.member .role{position:absolute;left:0;right:0;top:171px;font-size:12px}
.member p{position:absolute;left:22px;right:22px;top:194px;font-size:10.5px;line-height:1.5;font-weight:600}
.contact-bar{position:absolute;left:0;right:0;bottom:0;height:31px;background:#b5b5b5;display:flex;justify-content:center;align-items:center;gap:8px}
.member.current .contact-bar{background:var(--orange)}
.arrow{top:201px;width:72px;height:72px;border:3px solid #fff;border-radius:50%}
.arrow.left{left:39px;border-color:#f2f2f2}
.arrow.right{left:1085px}
.arrow svg{position:absolute;left:20px;top:16px}
.dots{left:558px;top:437px;display:flex;gap:12px}
.dots i{width:16px;height:16px;border-radius:50%;background:#bdbdbd}
.dots i:first-child{background:var(--orange)}

/* partners */
.partners{left:0;top:2003px;width:1200px;height:242px}
.partners .section-title{top:38px;color:var(--orange-text)}
.badge{background:#a7a7a7;top:135px}

/* footer */
.site-footer{left:0;top:2245px;width:1200px;height:386px;background:var(--dark);font-family:"Arimo",sans-serif;color:#fff}
.foot-col h5{color:var(--teal);font-size:16px;font-weight:700;letter-spacing:.3px}
.foot-col ul{list-style:none;margin-top:28px;font-size:14.5px;line-height:23.5px}
.contact-row{display:flex;align-items:center;gap:18px;font-size:14.5px;position:absolute;left:0}
.newsletter p{margin-top:30px;font-size:15.5px}
.email-field{margin-top:10px;width:215px;height:24px;background:#cfcfcf;font-size:14px;color:#888;padding-left:36px;line-height:24px;position:relative}
.email-field::before{content:"";position:absolute;left:10px;top:6px;width:16px;height:11px;background:#999}
.subscribe{margin:8px 0 0 118px;width:96px;height:24px;background:var(--lime);color:#333;font-size:14px;text-align:center;line-height:24px}
.legal{left:0;top:2631px;width:1200px;height:64px;background:var(--orange);color:#fff;font-family:"Arimo",sans-serif;font-size:11.5px;text-align:center;padding-top:18px;line-height:1.35}
</style>
</head>
<body>

<header class="site-header abs">
  <div class="brand abs"><span class="brand-mark"></span><span class="brand-name">MERIVALE CREST<br>TECHNOLOGY GROUP</span></div>
  <div class="enquiry abs">Make an Enquiry<span>+0123 456 789</span></div>
  <nav class="main-nav abs">
    <span class="active">Home</span><span>About</span><span>History</span><span>Our Team</span><span>Partners</span><span>Services</span><span>Contact Us</span>
  </nav>
</header>

<section class="hero abs" role="img" aria-label="Panoramic photograph of a city floating above the clouds at dusk"></section>
<div class="hero-panel abs">Your Text<br>Goes Here</div>
<div class="hero-caption abs">Panoramic image</div>
<div class="hero-rule abs"></div>

<div class="pill abs">WHO WE ARE</div>
<p class="who-text abs">Lorem Ipsum is simply dummy text of the printing and typesetting industry. Lorem Ipsum has been the industry's standard dummy text ever since the 1500s, when an unknown printer took a galley of type and scrambled it to make a type specimen book. It has survived not only five centuries, but also the leap into electronic typesetting, remaining essentially unchanged.</p>

<section class="services abs">
  <h2 class="section-title abs">OUR SERVICES</h2>
  <div class="service abs" style="left:137px">
    <svg width="80" height="60" viewBox="0 0 80 60" fill="none" stroke="#fff" stroke-width="3"><rect x="14" y="10" width="50" height="34"/><path d="M4 50h72"/><circle cx="39" cy="27" r="7"/></svg>
    <h3>IT Services</h3>
    <p>Lorem Ipsum is simply dummy text of the printing and typesetting industry. Lorem</p>
  </div>
  <div class="more abs" style="left:348px">View More</div>

  <div class="service abs" style="left:462px">
    <svg width="80" height="60" viewBox="0 0 80 60" fill="none" stroke="#fff" stroke-width="3"><path d="M4 20l14-8 14 6 12-6 14 4 18 10"/><path d="M22 30l16 14 8-4 10 4 12-12"/><path d="M30 36l8-8"/></svg>
    <h3>Business Solutions</h3>
    <p>Lorem Ipsum is simply dummy text of the printing and typesetting industry. Lorem</p>
  </div>
  <div class="more abs" style="left:670px">View More</div>

  <div class="service two abs" style="left:785px">
    <svg width="70" height="70" viewBox="0 0 70 70" fill="none" stroke="#fff" stroke-width="4"><circle cx="35" cy="35" r="28"/><circle cx="35" cy="35" r="11"/></svg>
    <h3>Software Implementation<br>&amp; Consulting</h3>
    <p>Lorem Ipsum is simply dummy text of the printing and typesetting industry. Lorem</p>
  </div>
  <div class="more abs" style="left:994px">View More</div>
</section>

<section class="team abs">
  <h2 class="section-title abs">MEET OUR TEAM</h2>
  <div class="arrow left abs"><svg width="26" height="36" viewBox="0 0 26 36" fill="none" stroke="#f2f2f2" stroke-width="3"><path d="M20 2L4 18l16 16"/></svg></div>

  <article class="member current abs" style="left:133px">
    <div class="avatar" role="img" aria-label="Portrait photo of team member"></div>
    <h4>Name Here</h4><div class="role">Designation</div>
    <p>Lorem Ipsum is simply dummy text of the printing and typesetting industry. Lorem Ipsum has been the industry's standard dummy text ever</p>
    <div class="contact-bar">
      <svg width="16" height="16" viewBox="0 0 16 16" fill="#fff"><path d="M3 1l3 3-2 2c1 2 3 4 5 5l2-2 3 3-2 3C7 15 1 9 1 3z"/></svg>
      <svg width="18" height="13" viewBox="0 0 18 13"><rect width="18" height="13" fill="#fff"/><path d="M1 1l8 6 8-6" stroke="var(--orange)" fill="none"/></svg>
      <svg width="15" height="15"><circle cx="7.5" cy="7.5" r="7.5" fill="#fff"/></svg>
      <svg width="15" height="15"><circle cx="7.5" cy="7.5" r="7.5" fill="#fff"/></svg>
    </div>
  </article>

  <article class="member abs" style="left:374px">
    <div class="avatar" role="img" aria-label="Portrait photo of team member"></div>
    <h4>Name Here</h4><div class="role">Designation</div>
    <p>Lorem Ipsum is simply dummy text of the printing and typesetting industry. Lorem Ipsum has been the industry's standard dummy text ever</p>
    <div class="contact-bar">
      <svg width="16" height="16" viewBox="0 0 16 16" fill="#fff"><path d="M3 1l3 3-2 2c1 2 3 4 5 5l2-2 3 3-2 3C7 15 1 9 1 3z"/></svg>
      <svg width="18" height="13" viewBox="0 0 18 13"><rect width="18" height="13" fill="#fff"/><path d="M1 1l8 6 8-6" stroke="#b5b5b5" fill="none"/></svg>
      <svg width="15" height="15"><circle cx="7.5" cy="7.5" r="7.5" fill="#fff"/></svg>
      <svg width="15" height="15"><circle cx="7.5" cy="7.5" r="7.5" fill="#fff"/></svg>
    </div>
  </article>

  <article class="member abs" style="left:611px">
    <div class="avatar" role="img" aria-label="Portrait photo of team member"></div>
    <h4>Name Here</h4><div class="role">Designation</div>
    <p>Lorem Ipsum is simply dummy text of the printing and typesetting industry. Lorem Ipsum has been the industry's standard dummy text ever</p>
    <div class="contact-bar">
      <svg width="16" height="16" viewBox="0 0 16 16" fill="#fff"><path d="M3 1l3 3-2 2c1 2 3 4 5 5l2-2 3 3-2 3C7 15 1 9 1 3z"/></svg>
      <svg width="18" height="13" viewBox="0 0 18 13"><rect width="18" height="13" fill="#fff"/><path d="M1 1l8 6 8-6" stroke="#b5b5b5" fill="none"/></svg>
      <svg width="15" height="15"><circle cx="7.5" cy="7.5" r="7.5" fill="#fff"/></svg>
      <svg width="15" height="15"><circle cx="7.5" cy="7.5" r="7.5" fill="#fff"/></svg>
    </div>
  </article>

  <article class="member abs" style="left:848px">
    <div class="avatar" role="img" aria-label="Portrait photo of team member"></div>
    <h4>Name Here</h4><div class="role">Designation</div>
    <p>Lorem Ipsum is simply dummy text of the printing and typesetting industry. Lorem Ipsum has been the industry's standard dummy text ever</p>
    <div class="contact-bar">
      <svg width="16" height="16" viewBox="0 0 16 16" fill="#fff"><path d="M3 1l3 3-2 2c1 2 3 4 5 5l2-2 3 3-2 3C7 15 1 9 1 3z"/></svg>
      <svg width="18" height="13" viewBox="0 0 18 13"><rect width="18" height="13" fill="#fff"/><path d="M1 1l8 6 8-6" stroke="#b5b5b5" fill="none"/></svg>
      <svg width="15" height="15"><circle cx="7.5" cy="7.5" r="7.5" fill="#fff"/></svg>
      <svg width="15" height="15"><circle cx="7.5" cy="7.5" r="7.5" fill="#fff"/></svg>
    </div>
  </article>

  <div class="arrow right abs"><svg width="26" height="36" viewBox="0 0 26 36" fill="none" stroke="#fff" stroke-width="3"><path d="M6 2l16 16-16 16"/></svg></div>
  <div class="dots abs"><i></i><i></i><i></i><i></i></div>
</section>

<section class="partners abs">
  <h2 class="section-title abs">OUR PARTNERS</h2>
  <div class="badge abs" style="left:143px;width:62px;height:62px;border-radius:50%;top:121px"></div>
  <div class="badge abs" style="left:278px;width:134px;height:26px;border-radius:4px;top:139px"></div>
  <div class="badge abs" style="left:487px;width:60px;height:50px;border-radius:4px;top:127px"></div>
  <div class="badge abs" style="left:636px;width:116px;height:14px;border-radius:7px;top:145px"></div>
  <div class="badge abs" style="left:816px;width:106px;height:26px;border-radius:4px;top:139px"></div>
  <div class="badge abs" style="left:990px;width:92px;height:30px;border-radius:4px;top:137px"></div>
</section>

<footer class="site-footer abs">
  <div class="foot-col abs" style="left:147px;top:84px;width:250px;height:200px">
    <h5>CONTACT US</h5>
    <div class="contact-row" style="top:50px">
      <svg width="16" height="22" viewBox="0 0 16 22" fill="var(--teal)"><path d="M8 0a8 8 0 0 1 8 8c0 6-8 14-8 14S0 14 0 8a8 8 0 0 1 8-8z"/><circle cx="8" cy="8" r="3" fill="var(--dark)"/></svg>
      <span>Your Address Goes Here</span></div>
    <div class="contact-row" style="top:107px">
      <svg width="18" height="18" viewBox="0 0 16 16" fill="var(--teal)"><path d="M3 1l3 3-2 2c1 2 3 4 5 5l2-2 3 3-2 3C7 15 1 9 1 3z"/></svg>
      <span>+0123 456 789</span></div>
    <div class="contact-row" style="top:148px">
      <svg width="18" height="13" viewBox="0 0 18 13"><rect width="18" height="13" fill="var(--teal)"/><path d="M1 1l8 6 8-6" stroke="var(--dark)" fill="none"/></svg>
      <span>Youremailaddressgoeshere</span></div>
    <div class="contact-row" style="top:180px;gap:10px">
      <svg width="22" height="22"><circle cx="11" cy="11" r="11" fill="#9a9a9a"/></svg>
      <svg width="22" height="22"><circle cx="11" cy="11" r="11" fill="#9a9a9a"/></svg>
    </div>
  </div>
  <div class="foot-col abs" style="left:440px;top:84px">
    <h5>CUSTOMER SERVICE</h5>
    <ul><li>Lorem Ipsum</li><li>Lorem Ipsum</li><li>Lorem Ipsum</li><li>Lorem Ipsum</li><li>Lorem Ipsum</li><li>Lorem Ipsum</li><li>Lorem Ipsum</li></ul>
  </div>
  <div class="foot-col abs" style="left:676px;top:84px">
    <h5>QUICK LINKS</h5>
    <ul><li>Faq</li><li>New</li><li>About Us</li><li>Privacy Policy</li><li>Terms of Use</li></ul>
  </div>
  <div class="foot-col newsletter abs" style="left:863px;top:84px;width:214px">
    <h5 style="text-align:right">NEWS LETTER SIGN UP</h5>
    <p>Subscribe to our News Letter</p>
    <div class="email-field">E-mail</div>
    <div class="subscribe">Subscribe</div>
  </div>
</footer>

<div class="legal abs">HOME | SITE MAP | POLICIES | ARTICLES | CONTACT US | PRINT THIS PAGE | RSS rss | TOP OF PAGE<br>COPYRIGHT © 2016 merivale crest</div>

</body>
</html>
```